Healthcare website - Diabetic Shoes - Vitacor - No Cost

I am looking to upgrade my website. I do not want to use Wordpress, Adobe Muse or another designing program. The code should be easily editable using textpad or VI. After the project is done I want to easily add my custom PHP code.

Features
Creative and Modern Design .
Fully responsive site for use on mobile devices
bootstrap, jquery

My current website is
www.stridewellfeet.com

Target Market(s)

Older people who have diabetes. Target market is +60 years old, but we do have younger people going to the site to help out their parents.

Industry/Entity Type

Healthcare

Coding

Coded - Design and coding required

Number of Pages Required

2 page

Colors

Designer to choose colors to be used in the design.

Requirements
Must have
• The code should be easily editable using textpad or VI. After the project is done I want to easily add my custom PHP code.
• The first page will be the home page and the other page I need is this form.
• https://www.stridewellfeet.com/stride-well-feet-do-i-qualify.php
Should not have
• I do not want to use Wordpress, Adobe Muse or another designing program.

```html
<!DOCTYPE html>
<html lang="en">
<head>
<meta charset="utf-8">
<title>Stride Well Feet — Diabetic Shoes Covered by Vitacor</title>
<link rel="stylesheet" href="https://fonts.googleapis.com/css2?family=Poppins:wght@300;400;500;600;700&family=Roboto:wght@300;400;500&display=swap">
<style>
:root{
  --green:#57bb4f;
  --green-soft:#e3f4e1;
  --blue:#2a9fd8;
  --blue-band:#4cb3e4;
  --ink:#333a41;
  --text:#5d646b;
  --muted:#9aa0a6;
  --line:#d9dcdf;
  --grey-band:#f2f2f3;
  --footer:#3b3e43;
  --white:#ffffff;
}
*{box-sizing:border-box;margin:0;padding:0}
html,body{width:1200px;height:3719px;overflow:hidden}
body{position:relative;background:var(--white);font-family:"Poppins",sans-serif;color:var(--text)}
.abs{position:absolute}

/* header */
.site-header{position:absolute;left:0;top:0;width:1200px;height:74px;background:var(--white);box-shadow:0 1px 3px rgba(0,0,0,.06);z-index:2}
.brand{position:absolute;left:87px;top:22px;display:flex;align-items:center;gap:9px;font-size:24px;font-weight:500;color:var(--green);letter-spacing:-.3px}
.brand-dot{width:14px;height:14px;border-radius:50%;background:var(--green)}
.main-nav{position:absolute;left:392px;top:28px;display:flex;gap:27px;font-size:13px;font-weight:500;color:var(--ink)}
.main-nav .active{color:var(--green)}
.main-nav .login{display:flex;align-items:center;gap:5px}

/* hero */
.hero{position:absolute;left:0;top:74px;width:1200px;height:484px;background:#fafafa}
.hero-sub{position:absolute;left:87px;top:177px;font-size:23px;font-weight:400;color:var(--ink)}
.hero-title{position:absolute;left:87px;top:210px;font-size:38px;font-weight:700;color:var(--ink)}
.hero-title span{color:var(--blue)}
.btn{display:flex;align-items:center;justify-content:center;font-size:13px;font-weight:500;border-radius:2px}
.btn-soft{background:var(--green-soft);color:var(--green)}
.btn-blue{background:var(--blue);color:var(--white)}
.hero .shop-now{position:absolute;left:87px;top:273px;width:111px;height:45px}
.hero-visual{position:absolute;left:434px;top:0;width:766px;height:460px;background:linear-gradient(160deg,#5b5f66 0%,#7c8088 35%,#3a3c40 60%,#9a5a33 85%,#c47a48 100%);border-radius:0 0 0 180px;opacity:.92}
.hero-dots{position:absolute;left:87px;top:430px;display:flex;gap:8px}
.hero-dots i{width:7px;height:7px;border-radius:50%;background:#cfd3d6}
.hero-dots i:first-child{background:var(--green)}

/* steps */
.steps{position:absolute;left:0;top:558px;width:1200px;height:379px;background:var(--green);color:var(--white)}
.steps-title{position:absolute;left:0;top:64px;width:1200px;text-align:center;font-size:19px;font-weight:400}
.steps-rule{position:absolute;left:580px;top:105px;width:40px;height:2px;background:var(--white)}
.step{position:absolute;top:148px;width:240px;text-align:center}
.step-icon{width:76px;height:76px;margin:0 auto;border-radius:50%;background:rgba(255,255,255,.18);display:flex;align-items:center;justify-content:center}
.step p{margin-top:30px;font-size:14px;line-height:1.6}

/* about */
.about-media{position:absolute;left:87px;top:1004px;width:396px;height:377px;background:linear-gradient(180deg,#2b2b34 0%,#4a4752 60%,#e2338f 100%);box-shadow:0 30px 30px -20px rgba(0,0,0,.25)}
.about-body{position:absolute;left:555px;top:1022px;width:555px}
.about-body h2{font-size:19px;font-weight:500;color:var(--ink)}
.rule-blue{width:40px;height:2px;background:var(--blue);margin:12px 0 22px}
.about-body p{font-size:11.5px;line-height:1.85;color:var(--text);margin-bottom:14px}
.about-body .learn{width:111px;height:45px;margin-top:16px}

/* catalog form */
.catalog-title{position:absolute;left:0;top:1452px;width:1200px;text-align:center;font-size:20px;font-weight:400;color:var(--ink)}
.field{position:absolute;width:323px}
.field label{display:block;font-size:13px;color:var(--ink);margin-bottom:10px}
.field .input{font-size:14px;color:var(--muted);padding-bottom:10px;border-bottom:1px solid var(--line);display:flex;justify-content:space-between}
.catalog-form .submit{position:absolute;left:533px;top:1978px;width:136px;height:45px;background:#e5f3fa;color:var(--blue);font-size:13px}

/* faq */
.faq{position:absolute;left:0;top:2087px;width:1200px;height:526px;background:var(--grey-band)}
.faq h2{position:absolute;left:0;top:65px;width:1200px;text-align:center;font-size:20px;font-weight:400;color:var(--ink)}
.faq .rule-blue{position:absolute;left:580px;top:106px;margin:0}
.faq-item{position:absolute;left:243px;width:712px;font-size:13px;color:var(--ink);display:flex;justify-content:space-between;align-items:center}
.faq-toggle{width:14px;height:14px;border-radius:50%;background:#d6d8da}
.faq-answer{position:absolute;left:243px;top:285px;width:712px;height:164px;background:var(--white);padding:30px 28px;font-size:11.5px;line-height:2;color:var(--text);box-shadow:0 2px 6px rgba(0,0,0,.06)}

/* video */
.video{position:absolute;left:0;top:2613px;width:1200px;height:439px;background:var(--blue-band)}
.video-art{position:absolute;left:120px;top:40px;width:960px;height:399px;background:linear-gradient(90deg,rgba(255,255,255,.05),rgba(255,255,255,.12) 50%,rgba(30,120,170,.15));border-radius:4px}
.play{position:absolute;left:555px;top:176px;width:90px;height:90px;border-radius:50%;background:var(--white);display:flex;align-items:center;justify-content:center}

/* products */
.products-title{position:absolute;left:0;top:3113px;width:1200px;text-align:center;font-size:20px;font-weight:400;color:var(--ink)}
.products .rule-blue{position:absolute;left:580px;top:3153px;margin:0}
.product{position:absolute;top:3198px;width:241px;height:290px;background:var(--white);border:1px solid #eceef0;text-align:center}
.product h3{margin-top:32px;font-size:13px;font-weight:500;color:var(--ink)}
.product .price{margin-top:6px;font-size:12px;color:var(--muted)}
.product .shot{margin:22px auto 0;width:110px;height:170px;background:linear-gradient(180deg,#3b3e44,#6b6f76)}
.product.featured{box-shadow:0 20px 30px rgba(0,0,0,.12);border-color:transparent}
.product.featured .shot{background:linear-gradient(180deg,#e8e8e8,#c9c9c9)}
.product .overlay-btn{position:absolute;left:52px;top:120px;width:136px;height:45px}
.view-more{position:absolute;left:521px;top:3533px;width:161px;height:42px}

/* footer */
.site-footer{position:absolute;left:0;top:3637px;width:1200px;height:82px;background:var(--footer);color:var(--white);text-align:center;font-size:11px;padding-top:22px;line-height:2}
.to-top{position:absolute;left:1135px;top:3617px;width:40px;height:40px;border-radius:50%;background:var(--green);display:flex;align-items:center;justify-content:center}
</style>
</head>
<body>

<header class="site-header">
  <div class="brand"><span class="brand-dot"></span>Stride Well Feet</div>
  <nav class="main-nav">
    <span class="active">Home</span>
    <span>Stride Well Feet! Do I Qualify</span>
    <span>Why diabetic shoes</span>
    <span>Shoes</span>
    <span>Products</span>
    <span>Shoe Fitter Jobs</span>
    <span>FAQ</span>
    <span class="login"><svg width="11" height="11" viewBox="0 0 12 12"><circle cx="6" cy="3.5" r="2.5" fill="#333a41"/><path d="M1 12c0-3 2.2-5 5-5s5 2 5 5z" fill="#333a41"/></svg>Log in</span>
  </nav>
</header>

<section class="hero">
  <div class="hero-visual" role="img" aria-label="Three diabetic shoes: a grey sneaker, a dark strap shoe and a brown leather shoe"></div>
  <p class="hero-sub">Diabetic Shoes or Sneakers</p>
  <h1 class="hero-title">Covered by <span>Vitacor</span></h1>
  <a class="btn btn-soft shop-now">Shop Now</a>
  <div class="hero-dots"><i></i><i></i><i></i><i></i></div>
</section>

<section class="steps">
  <h2 class="steps-title">4 Easy Steps To Receive Your New Therapeutic Shoes.</h2>
  <div class="steps-rule"></div>
  <div class="step" style="left:96px">
    <div class="step-icon"><svg width="30" height="34" viewBox="0 0 30 34" fill="none" stroke="#fff" stroke-width="1.6"><path d="M3 1h16l8 8v24H3z"/><path d="M19 1v8h8M8 15h14M8 20h14M8 25h10"/></svg></div>
    <p>Fill out an application to<br>see if you qualify.</p>
  </div>
  <div class="step" style="left:401px">
    <div class="step-icon"><svg width="34" height="26" viewBox="0 0 34 26" fill="none" stroke="#fff" stroke-width="1.6"><rect x="1" y="1" width="32" height="24" rx="2"/><path d="M1 8h32M6 15h10M6 19h6M22 15h6"/></svg></div>
    <p>A prescription will be<br>faxed to your primary physician.</p>
  </div>
  <div class="step" style="left:656px">
    <div class="step-icon"><svg width="36" height="20" viewBox="0 0 36 20" fill="none" stroke="#fff" stroke-width="1.6"><path d="M2 4l8 1 5 4 9 2c6 1 10 3 10 7H2z"/><path d="M2 15h32"/></svg></div>
    <p>After the prescription is signed, a<br>certified shoe fitter will fit your<br>new shoes.</p>
  </div>
  <div class="step" style="left:896px">
    <div class="step-icon"><svg width="32" height="30" viewBox="0 0 32 30" fill="none" stroke="#fff" stroke-width="1.6"><rect x="6" y="2" width="20" height="14"/><path d="M10 8l4 4 8-8M1 20h8l6 3h9M1 28h22l8-6"/></svg></div>
    <p>Enjoy your new shoes!</p>
  </div>
</section>

<section class="about">
  <div class="about-media" role="img" aria-label="Photo looking down at a pair of grey athletic shoes on a dark floor"></div>
  <div class="about-body">
    <h2>About Stride Well Feet</h2>
    <div class="rule-blue"></div>
    <p>Stride Well Feet was created by Meridian Health Supply to educate clients and prospective shoe fitters about diabetic shoes and the coverage that Vitacor provides. Founded by a Board-Certified Pedorthist, the company's mission is to help clients receive properly fitted shoes from qualified healthcare professionals around the United States. Meridian Health Supply works directly with Vitacor to determine the patient's coverage.</p>
    <p>At Meridian Health Supply, we understand the health benefits and medical safety associated with properly fitted shoes. We strive to educate clients about wearing appropriate footwear and avoiding unnecessary complications...</p>
    <a class="btn btn-blue learn">Learn More</a>
  </div>
</section>

<section class="catalog-form">
  <h2 class="catalog-title">Request a free diabetic shoe catalog</h2>
  <div class="field" style="left:87px;top:1532px"><label>First name:</label><div class="input">Enter your name</div></div>
  <div class="field" style="left:436px;top:1532px"><label>Last name:</label><div class="input">Enter your last name</div></div>
  <div class="field" style="left:786px;top:1532px"><label>Address:</label><div class="input">Enter your company name</div></div>
  <div class="field" style="left:87px;top:1621px"><label>City:</label><div class="input">Enter your city</div></div>
  <div class="field" style="left:436px;top:1621px"><label>State:</label><div class="input">Enter your state</div></div>
  <div class="field" style="left:786px;top:1621px"><label>Zip:</label><div class="input">Enter your zip code</div></div>
  <div class="field" style="left:87px;top:1710px"><label>Phone:</label><div class="input">Enter your phone</div></div>
  <div class="field" style="left:436px;top:1710px"><label>Best time to call:</label><div class="input">Enter best time to call</div></div>
  <div class="field" style="left:786px;top:1710px"><label>Email:</label><div class="input">Enter email</div></div>
  <div class="field" style="left:87px;top:1802px;width:498px"><label>Primary Insurance:</label><div class="input">Vitacor<svg width="10" height="6" viewBox="0 0 10 6"><path d="M1 1l4 4 4-4" stroke="#888" fill="none"/></svg></div></div>
  <div class="field" style="left:597px;top:1802px;width:513px"><label>Do you want to check eligibility Online?</label><div class="input">Check eligibility<svg width="10" height="6" viewBox="0 0 10 6"><path d="M1 1l4 4 4-4" stroke="#888" fill="none"/></svg></div></div>
  <div class="field" style="left:87px;top:1891px;width:1023px"><label>Comments:</label><div class="input">Enter your city</div></div>
  <a class="btn submit">Request Catalog</a>
</section>

<section class="faq">
  <h2>Frequently Asked Questions</h2>
  <div class="rule-blue"></div>
  <div class="faq-item" style="top:150px">How Does Diabetes Cause Foot Problems?<span class="faq-toggle"></span></div>
  <div class="faq-item" style="top:195px">Why Are Properly Fitted Shoes Important?<span class="faq-toggle"></span></div>
  <div class="faq-item" style="top:240px">How Do You Know If Orthopedic Shoes Are Right For You?<span class="faq-toggle"></span></div>
  <div class="faq-answer">Anyone with Diabetic Neuropathy, poor circulation, high risk of infection or nerve damage can benefit from diabetic socks and our shoes. Vitacor patients who qualify are eligible for one pair of shoes and three sets of custom insoles per year - at no out of pocket cost to them. Additionally, most private insurance companies will cover the same benefits as Vitacor.</div>
</section>

<section class="video">
  <div class="video-art" role="img" aria-label="Line illustration of a doctor at a laptop with forms and a shoe on a board"></div>
  <div class="play"><svg width="26" height="30" viewBox="0 0 26 30"><path d="M3 2l21 13L3 28z" fill="#3b3e43"/></svg></div>
</section>

<section class="products">
  <h2 class="products-title">Vitacor Products</h2>
  <div class="rule-blue"></div>
  <article class="product" style="left:89px"><h3>Tens Unit</h3><p class="price">from $120.25</p><div class="shot" role="img" aria-label="TENS unit with electrode pads"></div></article>
  <article class="product featured" style="left:350px"><h3>Seat Lift</h3><p class="price">from $120.25</p><div class="shot" role="img" aria-label="Seat lift cushion"></div><a class="btn btn-blue overlay-btn">Request Catalog</a></article>
  <article class="product" style="left:610px"><h3>Back Brace</h3><p class="price">from $120.25</p><div class="shot" role="img" aria-label="Back brace" style="background:linear-gradient(180deg,#4a5058,#6fb7e0)"></div></article>
  <article class="product" style="left:870px"><h3>Knee, Ankle, Wrist, Braces</h3><p class="price">from $120.25</p><div class="shot" role="img" aria-label="Knee, ankle and wrist braces"></div></article>
  <a class="btn btn-soft view-more">View More Products</a>
</section>

<a class="to-top"><svg width="14" height="9" viewBox="0 0 14 9"><path d="M1 8l6-6 6 6" stroke="#fff" stroke-width="2" fill="none"/></svg></a>
<footer class="site-footer">
  <p>© Copyright Stride Well Feet - All Rights Reserved, Co-payments, deductibles and some restrictions apply.</p>
  <p>* Co-payments, deductibles and some restrictions apply. &nbsp;•&nbsp; Terms of use &nbsp;•&nbsp; Privacy Policy</p>
</footer>

</body>
</html>
```